Web Design Project

We have screen protector brand for mobile phone and we need
Looking for talented web designer. We need only graphic design of 3 page design Home, Catalog page and Product page

- Home page
- There will be rotating banners on the home page
- Top menu will have Hot products, Screen Protectors, Videos, Contact us
- Screen Protectors will be submenu
- Website will be two languages so put US and Turkish flags on the corner so users will be able to switch
- Home page, there will be newest products and hot products and also one video

I also live any additional creative idea for the website
There will be one inner page and catalog page

Check existing page www.vendrox.com which looks pretty bad. You can take logo from there. If you need logo separate i can send it.

I have attached the layout but feel free to change it. I only try to give idea what i wanna see on it.

```html
<!DOCTYPE html>
<html lang="en">
<head>
<meta charset="utf-8">
<title>Vendrox – Screen Protectors</title>
<link rel="stylesheet" href="https://fonts.googleapis.com/css2?family=Oswald:wght@300;400;500&family=Open+Sans:wght@400;600;700&display=swap">
<style>
:root{
  --orange:#e8521a;
  --blue:#1e8fe6;
  --ink:#333;
  --muted:#777;
  --line:#e2e2e2;
  --panel:#f1f1f1;
  --backdrop:#8a8a8a;
  --footer:#4a4a4a;
  --white:#fff;
}
*{box-sizing:border-box;margin:0;padding:0}
html,body{width:733px;height:1200px;overflow:hidden}
body{background:var(--backdrop);font-family:"Open Sans",Arial,sans-serif;color:var(--ink);position:relative}
.page{position:absolute;left:92px;top:0;width:549px;height:1200px;background:var(--white)}
.abs{position:absolute}
.top-strip{left:0;top:0;width:549px;height:5px;background:var(--orange)}
.account-links{right:33px;top:8px;font:400 9px "Oswald",sans-serif;color:#555;display:flex;gap:0}
.account-links span{padding:0 9px;border-left:1px solid #bbb;line-height:10px}
.account-links span:first-child{border-left:0}
.account-links .signup{color:var(--orange);padding-right:0}
.brand{left:25px;top:36px;display:flex;align-items:center;gap:6px;font:500 22px "Oswald",sans-serif;letter-spacing:1px;color:#333}
.brand i{display:block;width:14px;height:14px;background:var(--orange)}
.search-label{left:327px;top:35px;font:400 12px "Oswald",sans-serif;color:var(--blue)}
.search-box{left:369px;top:32px;width:150px;height:22px;border:1px solid #ccc;border-radius:2px;font-size:8px;font-style:italic;color:#999;padding:5px 6px}
.search-box svg{position:absolute;right:5px;top:4px}
.lang{left:455px;top:63px;font-size:8px;color:#aaa}
.lang b{color:var(--orange);font-weight:400}
.nav{left:20px;top:89px;width:509px;height:22px;background:var(--panel);display:flex;align-items:center}
.nav .home{width:21px;height:22px;background:var(--orange);display:flex;align-items:center;justify-content:center}
.nav a{font:400 11px "Oswald",sans-serif;color:#333;text-decoration:none;padding:0 6px;height:22px;line-height:22px}
.nav a.on{background:var(--blue);color:#fff;margin-left:4px;padding:0 8px}
.social{position:absolute;right:8px;top:3px;display:flex;gap:5px}
.social i{display:block;width:16px;height:16px;border-radius:50%;background:#9aa3ad}
.rule{left:0;width:549px;height:1px;background:var(--line)}
.hero{left:20px;top:125px;width:509px;height:286px;background:linear-gradient(135deg,#4b5361,#2a3140 60%,#3a4252)}
.hero-panel{background:rgba(110,118,130,.75);color:#fff;padding:10px 10px}
.hero-panel h3{font:300 16px "Oswald",sans-serif;color:var(--orange);margin-bottom:4px}
.hero-panel p{font:300 13px/17px "Oswald",sans-serif}
.hero-panel p b{font-weight:500}
.btn{background:var(--blue);color:#fff;font:400 10px "Open Sans",sans-serif;text-align:center}
.slider{left:20px;top:413px;width:509px;height:11px;display:flex;gap:2px}
.slider span{flex:1;background:#ccc}
.slider span.on{background:var(--orange)}
.sec-title{font:400 14px "Oswald",sans-serif;color:var(--blue)}
.sec-line{height:1px;background:var(--line)}
.sec-line::before{content:"";display:block;width:100%;height:1px}
.video{left:23px;top:487px;width:246px;height:184px;background:linear-gradient(160deg,#9bc46e,#6b9a45);border:3px solid #eee}
.video .play{position:absolute;left:99px;top:68px}
.video-text{left:24px;top:689px;width:245px;border-left:2px solid #ddd;padding-left:9px;font-size:9px;line-height:12.5px;color:#888;text-align:justify}
.why-intro{left:300px;top:486px;width:230px;font-size:9px;line-height:13px}
.benefit{left:300px;width:229px;display:flex;gap:11px}
.benefit .ico{flex:0 0 41px;height:41px;border-radius:50%;background:#e6e6e6;border:2px solid #d0d0d0;display:flex;align-items:center;justify-content:center}
.benefit h4{font:400 11px "Oswald",sans-serif;color:var(--orange);margin-bottom:1px}
.benefit p{font-size:9px;line-height:12px;color:#444}
.arrows{left:496px;top:806px;display:flex;gap:12px}
.card{top:836px;width:118px;height:164px;border:3px solid #eee}
.card .shot{position:absolute;left:32px;top:6px;width:50px;height:106px;background:linear-gradient(180deg,#555,#222);border-radius:5px}
.card .name{position:absolute;left:0;right:0;top:115px;text-align:center;font-size:9px}
.card .price{position:absolute;left:6px;top:134px;font:700 14px "Open Sans",sans-serif;color:var(--orange)}
.card .btn{position:absolute;right:6px;top:134px;width:52px;height:18px;line-height:18px;font-size:8.5px}
.hover-note{position:absolute;left:4px;top:4px;width:104px;font-size:8px;line-height:17px;text-align:center;color:#222}
.footer{left:0;top:1052px;width:549px;height:125px;background:var(--footer);color:#eee}
.fcol{position:absolute;top:14px;font-size:8.5px;line-height:17px}
.fcol h5{font:400 11px "Oswald",sans-serif;color:var(--orange);margin-bottom:5px}
.fcol .addr{line-height:12px;font-weight:600}
.fcol .tel{line-height:11px;margin-top:8px}
.fcol li{list-style:none;font-weight:600}
.news-input{width:120px;height:15px;background:#fff;color:#999;font-size:7px;font-style:italic;padding:3px 5px;margin-top:4px}
.news-btn{margin:4px 0 0 67px;width:53px;height:15px;line-height:15px;font-size:8px}
.bottom{left:0;top:1177px;width:549px;height:23px;font-size:8px;color:#444;display:flex;justify-content:space-between;align-items:center;padding:0 20px}
</style>
</head>
<body>
<div class="page">
  <div class="abs top-strip"></div>
  <div class="abs account-links"><span>MY ACCOUNT</span><span>MY CART</span><span class="signup">SIGN UP</span></div>
  <div class="abs brand"><i></i>VENDROX</div>
  <div class="abs search-label">SEARCH:</div>
  <div class="abs search-box">type your keyword here...
    <svg width="12" height="12" viewBox="0 0 12 12"><circle cx="5" cy="5" r="3.5" fill="none" stroke="#e8521a" stroke-width="1.8"/><line x1="7.5" y1="7.5" x2="11" y2="11" stroke="#e8521a" stroke-width="2"/></svg>
  </div>
  <div class="abs lang"><b>english</b> | turkish</div>

  <nav class="abs nav">
    <span class="home"><svg width="12" height="11" viewBox="0 0 12 11"><path d="M6 0L0 5h2v6h3V7h2v4h3V5h2z" fill="#fff"/></svg></span>
    <a class="on">HOT PRODUCTS</a><a>SCREEN PROTECTORS</a><a>VIDEOS</a><a>CONTACT US</a>
    <div class="social"><i></i><i></i><i></i></div>
  </nav>
  <div class="abs rule" style="top:117px"></div>

  <div class="abs hero" role="img" aria-label="Hand in a business suit holding a smartphone"></div>
  <div class="abs hero-panel" style="left:275px;top:143px;width:234px;height:140px">
    <h3>Cool Screen Protectors</h3>
    <p>- Anti-<b>scratch</b><br>- Anti-<b>fingerprint</b><br>- Washable<br>- Easy to <b>Apply</b></p>
    <div class="abs btn" style="right:8px;bottom:8px;width:80px;height:20px;line-height:20px">watch a video</div>
  </div>
  <div class="abs hero-panel" style="left:275px;top:291px;width:234px;height:104px">
    <h3>Free shipping</h3>
    <p>On order over <b>$29.98</b><br>(lower 48 states only)</p>
  </div>
  <div class="abs slider"><span class="on"></span><span></span><span></span></div>

  <h2 class="abs sec-title" style="left:20px;top:449px">WATCH OUR VIDEO PREVIEW</h2>
  <div class="abs sec-line" style="left:0;top:471px;width:278px"></div>
  <h2 class="abs sec-title" style="left:300px;top:449px">WHY CHOOSE US?</h2>
  <div class="abs sec-line" style="left:290px;top:471px;width:259px;background:#f3c3ae"></div>

  <div class="abs video" role="img" aria-label="Hands holding a smartphone over green grass">
    <svg class="play" width="48" height="48" viewBox="0 0 48 48"><circle cx="24" cy="24" r="21" fill="rgba(0,0,0,.15)" stroke="#fff" stroke-width="3"/><path d="M19 14l15 10-15 10z" fill="#fff"/></svg>
  </div>
  <p class="abs video-text">The preview video shows how our screen protectors work, and how to apply them to your device. Faucibus et congue vel, hendrerit non orci. Nunc lacus felis, accumsan in bibendum et, vehicula et arcu. Vestibulum ullamcorper purus non quam porttitor pellentesque.</p>

  <p class="abs why-intro">Because we sell high quality screen protectors.<br>Here are our screen protector's benefits:</p>
  <div class="abs benefit" style="top:521px">
    <span class="ico"><svg width="18" height="20" viewBox="0 0 18 20"><path d="M9 1l7 3v6c0 5-3 8-7 9-4-1-7-4-7-9V4z" fill="#b5b5b5"/></svg></span>
    <div><h4>ANTI - SCRATCH</h4><p>Anti-scratch is really cool, because maecenas tincidunt nisl eget diam porttitor at vulputate dui egestas. Donec ac elit nisi.</p></div>
  </div>
  <div class="abs benefit" style="top:586px">
    <span class="ico"><svg width="20" height="20" viewBox="0 0 20 20"><circle cx="10" cy="10" r="6" fill="none" stroke="#b5b5b5" stroke-width="2"/><line x1="3" y1="3" x2="17" y2="17" stroke="#e8521a" stroke-width="2"/><line x1="17" y1="3" x2="3" y2="17" stroke="#e8521a" stroke-width="2"/></svg></span>
    <div><h4>ANTI - FINGERPRINT</h4><p>Anty-fingerprint is really cool, because maecenas tincidunt nisl eget diam porttitor at vulputate dui egestas.</p></div>
  </div>
  <div class="abs benefit" style="top:650px">
    <span class="ico"><svg width="16" height="20" viewBox="0 0 16 20"><path d="M8 1C5 7 2 10 2 13a6 6 0 0012 0c0-3-3-6-6-12z" fill="#b5b5b5"/></svg></span>
    <div><h4>WASHABLE</h4><p>Our screen protectors are washable, and fermentum pretium nisl. Sed gravida volutpat risus quis suscipit.</p></div>
  </div>
  <div class="abs benefit" style="top:716px">
    <span class="ico"><svg width="20" height="20" viewBox="0 0 20 20"><path d="M3 17l2-6 9-9 4 4-9 9z" fill="#b5b5b5"/></svg></span>
    <div><h4>EASY TO APPLY</h4><p>Our screen protectors are really easy to apply for your device, ros eu neque ultrices laoreet. Vestibulum lectus justo.</p></div>
  </div>

  <h2 class="abs sec-title" style="left:20px;top:802px">NEW PRODUCTS</h2>
  <div class="abs sec-line" style="left:0;top:824px;width:549px"></div>
  <div class="abs arrows">
    <svg width="9" height="12" viewBox="0 0 9 12"><path d="M7 1L2 6l5 5" fill="none" stroke="#1e8fe6" stroke-width="2.5"/></svg>
    <svg width="9" height="12" viewBox="0 0 9 12"><path d="M2 1l5 5-5 5" fill="none" stroke="#1e8fe6" stroke-width="2.5"/></svg>
  </div>

  <div class="abs card" style="left:20px">
    <p class="hover-note">This is a hover info box. Here can be a product desc. If the user clicks here, he navigates to another page, where is a larger picture and more details.</p>
    <div class="name">Vendrox NOVA 3D</div><div class="price">$20.99</div><div class="btn">add to cart</div>
  </div>
  <div class="abs card" style="left:150px">
    <div class="shot" role="img" aria-label="Touchscreen smartphone"></div>
    <div class="name">Vendrox NOVA 3D</div><div class="price">$15.99</div><div class="btn">add to cart</div>
  </div>
  <div class="abs card" style="left:280px">
    <div class="shot" style="left:38px;top:20px;width:38px;height:80px" role="img" aria-label="Keyboard smartphone"></div>
    <div class="name">Vendrox NOVA 3D</div><div class="price">$17.99</div><div class="btn">add to cart</div>
  </div>
  <div class="abs card" style="left:410px">
    <div class="shot" style="left:30px;top:8px;width:54px;height:96px" role="img" aria-label="Keyboard smartphone with screen protector"></div>
    <div class="name">Vendrox NOVA 3D</div><div class="price">$16.99</div><div class="btn">add to cart</div>
  </div>

  <footer class="abs footer">
    <div class="fcol" style="left:20px;width:110px">
      <h5>CONTACT US</h5>
      <p class="addr">Deniz Sok. 18/5 Karaköy /<br>Istanbul - Turkey</p>
      <p class="tel">Tel: 0212 000 41 27<br>Fax: 0212 000 41 28<br>Email: info@vendrox.com</p>
    </div>
    <div class="fcol" style="left:149px">
      <h5>QUICK LINKS</h5>
      <ul><li>About Us</li><li>About screen protectors</li><li>Privacy Policy</li><li>Sitemap</li></ul>
    </div>
    <div class="fcol" style="left:280px">
      <h5>SUPPORT</h5>
      <ul><li>How to apply</li><li>FAQ</li><li>Warranty</li><li>Returning policy</li><li>Unsubscribe</li></ul>
    </div>
    <div class="fcol" style="left:409px">
      <h5>NEWSLETTER</h5>
      <p style="font-weight:600">Fresh news, discounts, sales:</p>
      <div class="news-input">type your e-mail address here...</div>
      <div class="btn news-btn">subscribe</div>
    </div>
  </footer>
  <div class="abs bottom"><span>Copyright © 2013 Vendrox.com</span><span>All rights reserved.</span></div>
</div>
</body>
</html>
```